Fast Money - Simple Book Cover Design

Hello,

I am in need of a cover for my new book. The Book Title Is

"Standing Growth - Keys to Glowing Customer Ratings That Fill The Calendar and Draw Fresh Clients Through Every Entrance!"

Author: Fireman Dale Orsworth

What I want: This is a book for businesses on improving their online reputation. I want to have 5 Stars on the cover. You can look at this quarvex search for ideas of what I am meaning.....

(copy and paste)

http://www.quarvex-find.example/search?q=5+star+online+reviews&mode=images&ref=kx7Lp2QwZt9 (copy and paste)

I am open to different color schemes for the book. I am partial to dark blues if you make it look good. Here is another book that I really like the cover of....

http://www.brindlemart.example/Clipwave-Tactics-Earning-Promotion-ebook/item/Z93KT4WQPX

I want the cover BOLD and to STAND OUT.

I am looking for a design to help establish me as an authority for online reputation marketing. This book will be both in Pagely format and be used in print as well.

I am open to questions....

Thanks!

Dale

Reason: I don't believe we have received the right designs. I am going to give everyone more time...

Reason: Hi everyone, I had some stuff come up and was not able to be involved in this project. I am extending because we have not seen the exact thing we want and need time to work with designers to get it right. Thanks Dale

Reason: I am currently traveling and can't wrap this up until I get back.

Target Market(s)

Business Owners

Industry/Entity Type

Business

Requirements
Must have
• Title and Subtitle

Author Name

5 Stars Images....
Nice to have
• Creativity

Bold and stand out

Professional

Should not have
• thin text, small to read text, lame graphics,

```html
<!DOCTYPE html>
<html lang="en">
<head>
<meta charset="utf-8">
<title>Standing Growth – Book Cover</title>
<link rel="stylesheet" href="https://fonts.googleapis.com/css2?family=Montserrat:wght@900&family=Roboto:wght@700;900&display=swap">
<style>
  :root {
    --navy-light: #1f4d76;
    --navy-mid: #123353;
    --navy-dark: #081626;
    --title-gold: #f7b818;
    --title-white-top: #ffffff;
    --title-white-bottom: #d6e4f2;
    --subtitle: #ffffff;
    --accent-gold: #f7b818;
    --author: #9aa9ba;
    --bar-track: rgba(255,255,255,0.14);
  }
  html, body {
    margin: 0;
    padding: 0;
    width: 800px;
    height: 1200px;
    overflow: hidden;
    background: var(--navy-dark);
  }
  .cover {
    position: relative;
    width: 800px;
    height: 1200px;
    overflow: hidden;
    background: radial-gradient(ellipse 75% 55% at 50% 42%, var(--navy-light) 0%, var(--navy-mid) 45%, var(--navy-dark) 100%);
    font-family: "Roboto", Arial, sans-serif;
    text-align: center;
  }
  .title {
    position: absolute;
    left: 0;
    right: 0;
    top: 86px;
    margin: 0;
    font-family: "Montserrat", Arial, sans-serif;
    font-weight: 900;
    line-height: 1;
    letter-spacing: 2px;
    text-transform: uppercase;
  }
  .title-line {
    display: block;
    font-size: 104px;
  }
  .title-line--gold {
    color: var(--title-gold);
    text-shadow: 0 3px 6px rgba(0,0,0,0.35);
  }
  .title-line--white {
    margin-top: 10px;
    background: linear-gradient(180deg, var(--title-white-top) 0%, var(--title-white-bottom) 100%);
    -webkit-background-clip: text;
    background-clip: text;
    color: transparent;
    filter: drop-shadow(0 3px 5px rgba(0,0,0,0.35));
  }
  .rating-graphic {
    position: absolute;
    left: 170px;
    top: 360px;
    width: 460px;
    height: 400px;
  }
  .subtitle {
    position: absolute;
    left: 0;
    right: 0;
    top: 830px;
    margin: 0;
    color: var(--subtitle);
    font-weight: 700;
    line-height: 1.25;
    white-space: nowrap;
    text-shadow: 0 2px 4px rgba(0,0,0,0.4);
  }
  .subtitle-line {
    display: block;
    font-size: 34px;
  }
  .subtitle-line--strong {
    font-size: 37px;
    margin-top: 4px;
  }
  .subtitle-accent {
    color: var(--accent-gold);
    font-weight: 900;
    font-size: 44px;
  }
  .author {
    position: absolute;
    left: 0;
    right: 0;
    top: 1086px;
    margin: 0;
    color: var(--author);
    font-weight: 700;
    font-size: 34px;
  }
</style>
</head>
<body>
<main class="cover">
  <h1 class="title">
    <span class="title-line title-line--gold">Standing</span>
    <span class="title-line title-line--white">Growth</span>
  </h1>

  <svg class="rating-graphic" viewBox="0 0 460 400" role="img" aria-label="Five gold stars above a rating distribution bar chart">
    <defs>
      <linearGradient id="star-gold" x1="0" y1="0" x2="1" y2="1">
        <stop offset="0" stop-color="#fff1b0"/>
        <stop offset="0.45" stop-color="#e8b93a"/>
        <stop offset="1" stop-color="#a8740f"/>
      </linearGradient>
      <linearGradient id="bar-gold" x1="0" y1="0" x2="1" y2="0">
        <stop offset="0" stop-color="#e8b93a"/>
        <stop offset="1" stop-color="#f9d463"/>
      </linearGradient>
      <symbol id="star" viewBox="0 0 100 100">
        <polygon points="50,3 61,37 97,37 68,59 79,94 50,72 21,94 32,59 3,37 39,37"/>
      </symbol>
    </defs>

    <g class="star-row" fill="url(#star-gold)">
      <use href="#star" x="4"   y="30" width="76" height="76"/>
      <use href="#star" x="94"  y="10" width="84" height="84"/>
      <use href="#star" x="184" y="0"  width="92" height="92"/>
      <use href="#star" x="282" y="10" width="84" height="84"/>
      <use href="#star" x="380" y="30" width="76" height="76"/>
    </g>

    <g class="bar-chart">
      <rect x="20" y="160" width="420" height="26" rx="13" fill="var(--bar-track)"/>
      <rect x="20" y="160" width="390" height="26" rx="13" fill="url(#bar-gold)"/>

      <rect x="20" y="206" width="420" height="26" rx="13" fill="var(--bar-track)"/>
      <rect x="20" y="206" width="250" height="26" rx="13" fill="url(#bar-gold)"/>

      <rect x="20" y="252" width="420" height="26" rx="13" fill="var(--bar-track)"/>
      <rect x="20" y="252" width="130" height="26" rx="13" fill="url(#bar-gold)"/>

      <rect x="20" y="298" width="420" height="26" rx="13" fill="var(--bar-track)"/>
      <rect x="20" y="298" width="64" height="26" rx="13" fill="url(#bar-gold)"/>

      <rect x="20" y="344" width="420" height="26" rx="13" fill="var(--bar-track)"/>
      <rect x="20" y="344" width="30" height="26" rx="13" fill="url(#bar-gold)"/>
    </g>
  </svg>

  <p class="subtitle">
    <span class="subtitle-line">Keys To <span class="subtitle-accent">Glowing</span> Customer Ratings</span>
    <span class="subtitle-line">That Fill The Calendar and Draw</span>
    <span class="subtitle-line subtitle-line--strong">Fresh Clients Through Every Entrance!</span>
  </p>

  <p class="author">Fireman Dale Orsworth</p>
</main>
</body>
</html>
```